First of a series of workplace posters- our values statement

To produce a high quality poster of our values, we would like one in a3 and one in a4 both full colour
By utilising the supplied text , the intent is to produce a really striking poster for all our work places, which set out our company values. we are looking for really strong graphical elements which support the message visually . This will be the first of a series of posters, so we are looking to establish at stylistic theme for all with this one. for more on our business,

Target Market(s)

Internal and external audiences, our clients are all tier one companies

Requirements
Must have
• contemporary design rather than conservative, visually striking
• Must be clearly readable from a reasonable distance
Nice to have
• would be nice to tie in to the blue and greens of our logo in similar fashion to our website. www.kbtgreenworks.com
Should not have
• Difficult to read fonts,

```html
<!DOCTYPE html>
<html lang="en">
<head>
<meta charset="utf-8">
<title>Our Values – KBT Greenworks</title>
<link href="https://fonts.googleapis.com/css2?family=Archivo:ital,wght@1,800&family=Roboto+Condensed:ital,wght@0,400;0,700;1,400;1,700&display=swap" rel="stylesheet">
<style>
  :root {
    --navy: #1f3479;
    --navy-deep: #18296a;
    --green: #6ab344;
    --paper: #ffffff;
    --ink: #1f3479;
  }
  html, body { margin: 0; padding: 0; overflow: hidden; background: var(--paper); }
  .poster {
    position: relative; width: 854px; height: 1200px; overflow: hidden;
    background: var(--paper); color: var(--ink);
    font-family: "Roboto Condensed", "Arial Narrow", sans-serif;
  }
  .backdrop { position: absolute; inset: 0; }
  .line { position: absolute; white-space: nowrap; margin: 0; }
  .title {
    font-family: "Archivo", "Arial Black", sans-serif; font-style: italic; font-weight: 800;
    font-size: 47px; letter-spacing: 0.5px; color: var(--navy); left: 262px; top: 80px;
  }
  .lead { font-style: italic; font-weight: 700; font-size: 15px; text-transform: uppercase; }
  .heading { font-style: italic; font-size: 19px; }
  .body { font-size: 15px; }
  .point { font-size: 12.5px; text-transform: uppercase; }
  .closing { font-style: italic; font-weight: 700; font-size: 14.5px; text-transform: uppercase; }
  .site { font-size: 10px; font-weight: 700; left: 356px; top: 1171px; }
  .badge {
    position: absolute; border-radius: 50%; background: var(--navy);
    border: 3px solid var(--paper); box-sizing: border-box;
    display: flex; align-items: center; justify-content: center; color: var(--paper);
  }
  .badge-mark { border-radius: 50%; }
  .harm-figure { font-size: 40px; line-height: 1; text-align: center; }
  .harm-word { font-size: 17px; letter-spacing: 4px; display: block; text-align: center; margin-top: 4px; }
  .brand-name { font-weight: 700; font-size: 22px; letter-spacing: 1px; }
</style>
</head>
<body>
<main class="poster">
  <svg class="backdrop" width="854" height="1200" viewBox="0 0 854 1200" aria-hidden="true">
    <path d="M0 0 L300 0 Q110 40 0 235 Z" fill="var(--navy)"/>
    <path d="M0 0 L170 0 Q60 40 0 120 Z" fill="var(--paper)"/>
    <path d="M700 0 L854 0 L854 120 Q800 30 700 0 Z" fill="var(--navy)"/>
    <path d="M0 560 Q40 980 330 1200 L215 1200 Q30 1020 0 760 Z" fill="var(--navy)"/>
    <path d="M230 40 C500 -10 760 20 830 95 C610 250 440 450 405 700 C385 880 415 1040 440 1125 C300 1000 200 850 188 650 C178 420 196 220 230 40 Z" fill="var(--green)"/>
  </svg>

  <h1 class="line title">OUR VALUES</h1>
  <p class="line lead" style="left:372px;top:150px">These are the key things we value.</p>
  <p class="line lead" style="left:357px;top:174px">We measure all our daily activities against these.</p>
  <p class="line lead" style="left:343px;top:198px">They define the way we do business.</p>

  <div class="badge" style="left:140px;top:208px;width:126px;height:126px">
    <div class="badge-mark" role="img" aria-label="Diamond icon" style="width:70px;height:44px;border-radius:4px;background:linear-gradient(#e6ecf7,#9fb0d4)"></div>
  </div>
  <h2 class="line heading" style="left:331px;top:222px">We value our people above everything else</h2>
  <p class="line body" style="left:318px;top:249px">We demonstrate this by:</p>
  <p class="line point" style="left:310px;top:268px">• Providing safe, positive, enjoyable workplaces where everyone feels</p>
  <p class="line point" style="left:316px;top:283px">valued and respected.</p>
  <p class="line point" style="left:296px;top:299px">• Providing careers, not jobs, we grow together.</p>
  <p class="line point" style="left:288px;top:314px">• Encouraging inclusion, participation and collaboration.</p>
  <p class="line point" style="left:283px;top:329px">• Recognising and rewarding contribution and excellence.</p>
  <p class="line point" style="left:278px;top:344px">• Supporting our people through tough times.</p>
  <p class="line point" style="left:274px;top:359px">• Fostering healthy work life balance.</p>

  <div class="badge" style="left:70px;top:405px;width:132px;height:132px">
    <span><span class="harm-figure">0%</span><span class="harm-word">HARM</span></span>
  </div>
  <h2 class="line heading" style="left:266px;top:376px">All our workplaces are safe work places</h2>
  <p class="line body" style="left:258px;top:402px">There is nothing more important to us than our team members going home healthy</p>
  <p class="line body" style="left:268px;top:419px">and safe every day, we won’t accept anything less. We believe workplace</p>
  <p class="line body" style="left:250px;top:436px">Safety is a management choice, by providing safe work systems and education we</p>
  <p class="line body" style="left:245px;top:453px">achieve our daily goal of zero harm.</p>
  <p class="line body" style="left:240px;top:470px">We:</p>
  <p class="line point" style="left:236px;top:489px">• Take the time to make our work areas safe, whatever it takes.</p>
  <p class="line point" style="left:238px;top:504px">• Don’t accept shortcuts.</p>
  <p class="line point" style="left:231px;top:519px">• Look out for each other.</p>
  <p class="line point" style="left:229px;top:534px">• Investigate our incidents and learn from them, no repeats.</p>
  <p class="line point" style="left:226px;top:549px">• Are constantly looking for ways to improve the safety of our workplaces and</p>
  <p class="line point" style="left:232px;top:564px">the health of our team members.</p>
  <p class="line point" style="left:220px;top:579px">• Think safe, work safe, go home safe!</p>

  <div class="badge" style="left:52px;top:597px;width:128px;height:128px">
    <div class="badge-mark" role="img" aria-label="Globe icon" style="width:76px;height:76px;background:radial-gradient(circle at 40% 40%,#f2f5fb,#9aaad0)"></div>
  </div>
  <h2 class="line heading" style="left:219px;top:598px">The planet benefits from our existence</h2>
  <p class="line body" style="left:214px;top:623px">We are relentlessly pursuing our objective of providing our clients with pathways to</p>
  <p class="line body" style="left:214px;top:640px">sustainable development. To achieve our vision,</p>
  <p class="line body" style="left:214px;top:657px">we:</p>
  <p class="line point" style="left:212px;top:678px">• Minimise our environmental impact in everything we do.</p>
  <p class="line point" style="left:212px;top:693px">• Actively develop and promote world’s best practices in rehabilitation of disturbed</p>
  <p class="line point" style="left:222px;top:708px">land.</p>

  <div class="badge" style="left:62px;top:788px;width:128px;height:128px">
    <span class="brand-name">KBT</span>
  </div>
  <h2 class="line heading" style="left:215px;top:728px">We are proud of who we are</h2>
  <p class="line body" style="left:215px;top:753px">Our reputation means the world to us.</p>
  <p class="line body" style="left:217px;top:770px">We:</p>
  <p class="line point" style="left:219px;top:791px">• Treat everyone with respect, and we expect it in return.</p>
  <p class="line point" style="left:221px;top:806px">• Follow the rules</p>
  <p class="line point" style="left:224px;top:821px">• Do what we say we will do.</p>
  <p class="line point" style="left:228px;top:836px">• Own our mistakes and we fix them.</p>
  <p class="line point" style="left:232px;top:851px">• Are trustworthy and transparent.</p>

  <h2 class="line heading" style="left:243px;top:869px">We set the standard</h2>
  <p class="line body" style="left:251px;top:895px">We are uncompromising on quality.</p>
  <p class="line body" style="left:257px;top:912px">We are the best at what we do, and we do what we are best at.</p>
  <p class="line body" style="left:266px;top:929px">We are always improving.</p>

  <div class="badge" style="left:180px;top:975px;width:126px;height:126px">
    <div class="badge-mark" role="img" aria-label="Joined hands icon" style="width:76px;height:76px;background:radial-gradient(circle,#eef2fa,#93a4cc)"></div>
  </div>
  <h2 class="line heading" style="left:280px;top:950px">We succeed together</h2>
  <p class="line body" style="left:293px;top:976px">We believe in win-win relationships. When our Business is profitable everyone</p>
  <p class="line body" style="left:303px;top:993px">benefits, our shareholders, employees, clients, suppliers and the community.</p>
  <p class="line heading" style="left:325px;top:1015px">AT KBT We:</p>
  <p class="line closing" style="left:345px;top:1040px">• Work as a team, we get it done together.</p>
  <p class="line closing" style="left:365px;top:1060px">• Are building on our success and growing together.</p>
  <p class="line closing" style="left:388px;top:1080px">• Choose to work with employees, customers, and</p>
  <p class="line closing" style="left:410px;top:1098px">suppliers who fit our values.</p>

  <p class="line site">www.kbtgreenworks.com</p>
</main>
</body>
</html>
```